Business Card Design

Our Motto is "Protecting Australia's Underground Utilities"

We want the Southern Cross inside a shield I have attached the southern cross and our old shield design

Product description is: Vacuum Excavation & Utility Location
Wet & Dry Vacuum Loading
Confined Space Entry Specialists
High Pressure Cleaning

The Southern Cross in the shield must be blue and white. The Company name must be Coastal Pipeguard Services. The Green & Gold Shield logo I uploaded is my OLD logo design. Thank you

Target Market(s)

Civil Construction

Industry/Entity Type

Business

Contact Information for Business Card

Coastal Pipeguard Services Pty Ltd
Corey Halbrook(Director)
0413862975
coreyh@pipeguardco.com.au
A.B.N.52938470116

Colors
0456a3

Requirements
Must have
• Southern Cross inside a shield, Blue and white design on the Southern Cross shield.
Must say Coastal Pipeguard Services P/L

```html
<!DOCTYPE html>
<html lang="en">
<head>
<meta charset="utf-8">
<title>Coastal Pipeguard Services – Business Card</title>
<link rel="stylesheet" href="https://fonts.googleapis.com/css2?family=Ubuntu:wght@400;500;700&display=swap">
<style>
  :root {
    --backdrop: #1b1b1b;
    --brand-blue: #0456a3;
    --card-blue: #1b5a9f;
    --sheen: rgba(255, 255, 255, 0.11);
    --card-white: #ffffff;
    --ink: #3a3a3a;
  }
  * { margin: 0; padding: 0; box-sizing: border-box; }
  html, body {
    width: 1200px;
    height: 999px;
    overflow: hidden;
    background: var(--backdrop);
    font-family: "Ubuntu", sans-serif;
  }
  .canvas {
    position: relative;
    width: 1200px;
    height: 999px;
  }
  .card {
    position: absolute;
    width: 572px;
    height: 353px;
    overflow: hidden;
  }

  /* Front */
  .card--front {
    left: 80px;
    top: 110px;
    background: var(--card-blue);
  }
  .card--front .sheen {
    position: absolute;
    inset: 0;
    width: 100%;
    height: 100%;
  }
  .motto {
    position: absolute;
    left: 134px;
    top: 150px;
    color: var(--card-white);
    font-weight: 500;
    font-size: 29px;
    line-height: 36px;
  }

  /* Back */
  .card--back {
    left: 548px;
    top: 530px;
    background: var(--card-white);
  }
  .person {
    position: absolute;
    left: 56px;
    top: 112px;
  }
  .person__name {
    color: var(--brand-blue);
    font-size: 17px;
    font-weight: 500;
    letter-spacing: 0.5px;
    text-transform: uppercase;
  }
  .person__role {
    color: var(--ink);
    font-size: 13px;
    margin-top: 1px;
  }
  .contacts {
    position: absolute;
    left: 56px;
    top: 176px;
    list-style: none;
  }
  .contacts li {
    display: flex;
    align-items: center;
    gap: 14px;
    height: 34px;
    margin-bottom: 10px;
    color: var(--ink);
    font-size: 13px;
  }
  .contacts .icon {
    width: 32px;
    height: 32px;
    background: var(--brand-blue);
    display: flex;
    align-items: center;
    justify-content: center;
    flex: none;
  }
  .brand {
    position: absolute;
    right: 44px;
    top: 132px;
    display: flex;
    align-items: center;
    gap: 12px;
    color: var(--brand-blue);
    font-weight: 700;
    font-size: 17px;
    line-height: 21px;
    text-transform: uppercase;
  }
  .brand__mark {
    width: 22px;
    height: 22px;
    border-radius: 50%;
    background: var(--brand-blue);
    flex: none;
  }
</style>
</head>
<body>
<main class="canvas">

  <section class="card card--front">
    <svg class="sheen" viewBox="0 0 572 353" preserveAspectRatio="none" aria-hidden="true">
      <path d="M0 0 H526 C470 140 300 270 0 318 Z" fill="var(--sheen)"/>
    </svg>
    <p class="motto">Protecting Australia's<br>Underground Utilities</p>
  </section>

  <section class="card card--back">
    <div class="person">
      <p class="person__name">Corey Halbrook</p>
      <p class="person__role">Director</p>
    </div>

    <ul class="contacts">
      <li>
        <span class="icon">
          <svg width="12" height="18" viewBox="0 0 12 18" aria-hidden="true">
            <rect x="1" y="1" width="10" height="16" rx="1.5" fill="none" stroke="#fff" stroke-width="1.6"/>
            <line x1="4.5" y1="14" x2="7.5" y2="14" stroke="#fff" stroke-width="1.4"/>
          </svg>
        </span>
        <span class="contacts__text">0413862975</span>
      </li>
      <li>
        <span class="icon">
          <svg width="16" height="14" viewBox="0 0 16 14" aria-hidden="true">
            <rect x="1" y="1" width="14" height="9" fill="none" stroke="#fff" stroke-width="1.6"/>
            <line x1="8" y1="10" x2="8" y2="13" stroke="#fff" stroke-width="1.6"/>
            <line x1="5" y1="13" x2="11" y2="13" stroke="#fff" stroke-width="1.6"/>
          </svg>
        </span>
        <span class="contacts__text">coreyh@pipeguardco.com.au</span>
      </li>
      <li>
        <span class="icon"></span>
        <span class="contacts__text">A.B.N.52938470116</span>
      </li>
    </ul>

    <div class="brand">
      <span class="brand__mark" aria-hidden="true"></span>
      <span class="brand__name">Coastal<br>Pipeguard<br>Services</span>
    </div>
  </section>

</main>
</body>
</html>
```